Marketplace Web Re-design overhaul @quarrynest

Hi,
We are currently in production with a website that is getting some mixed feedback about visual appeal and usability. We are using a responsive design and need to stay true to the logo colours and other marketing collateral we have in place. I will provide a brochure with the colour palate we use for some guidance. If you can please help us design something fresh and modern to communicate the essence of our company. The brochure will be a good summary of what we do and who we are targeting as customers. Our current website can be found at www.quarrynest.com. If there is any questions, please let me know.

Target Market(s)

Contractors and Corporate Companies

Industry/Entity Type

Information Technology

Number of Pages Required

4 page

Requirements
Must have
• Must have a complete new visual look, including
• 1. Images
• 2. Background colour scheme overhaul (not black)
• 3. re-design of the layout but keep to similar page breakdowns
Nice to have
• Some of the pages are a bit wordy, happy to have suggestions on how to reduce.
• Would be great if we can integrate the Plumb.ON! blog page to the Quarrynest page?
• This is some feedback a fellow UX designer provided to improve our CRO
• First off when you land on the home page, who is your audience? Are you everything to everyone? Even after watching the video (https://www.vidmarrow.net/watch?v=q7RtPe3LwZ0), I do not know what markets you service or who this app will be for.
• Your main headline and paragraph above the fold I find unnecessarily wordy and an overuse of 'buzzwords' . Perhaps you could look at appealing to the lowest common denominator and make it very simple and put it all into a simple sentence.
• The main hero image to the right of the headline offers no emotional pull at all. I'm assuming it's just a screenshot of your dashboard? Personally, I would be looking at using a person's image in that space.
• Also in this space, increase the size of your 'register' button. On the topic of your register button, you have it in different colours. Green in header, and red in content. Make it the same colour, and don't use that colour again on the site. That colour is to become your call to action (CTA) colour. Understandably you'll have three different colours for the account type, and again, don't use these colours anywhere else on the site.
• The registration area where the three account types are where you choose which one suits you, it's extremely busy with background images and heavy use of text. If you were my client, I would be advising you to ditch the bg image (including the Zelo shot), keeping the text, making the register icons much bigger. Perhaps instead of bg images, use a solid colour for each (green, orange, red). I'm highly confident this change will make a massive difference in your sign up rate.
Should not have
• Please keep to the fonts used on the original website
• Keep to the colour provided on the company brochure for guidance.

```html
<!DOCTYPE html>
<html lang="en">
<head>
<meta charset="utf-8">
<title>Quarrynest — Marketplace for Contractors and Companies</title>
<link href="https://fonts.googleapis.com/css2?family=Open+Sans:wght@300;400;600;700&display=swap" rel="stylesheet">
<style>
:root{
  --ink:#333333;
  --ink-soft:#555555;
  --muted:#777777;
  --panel:#efefef;
  --panel-deep:#e4e4e4;
  --white:#ffffff;
  --btn-grey:#8f8f8f;
  --accent:#f29a1f;
  --brand-green:#1d8a3f;
  --cta:#0b7a3e;
  --night:#1f2a33;
  --bar:#111111;
  --rule:#dddddd;
}
*{box-sizing:border-box;margin:0;padding:0}
html,body{width:1200px;height:3516px;overflow:hidden}
body{font-family:"Open Sans",Arial,sans-serif;color:var(--ink);background:var(--white);position:relative}
section,header,footer{position:absolute;left:0;width:1200px}
.photo{position:absolute}

/* header + hero */
.hero{top:0;height:731px;background:linear-gradient(120deg,#dfe3e8 0%,#c9cfd6 35%,#5a6470 70%,#2c3440 100%)}
.site-nav{top:0;height:63px;background:rgba(40,40,40,.55);z-index:2}
.brand{position:absolute;left:78px;top:10px;display:flex;align-items:center;gap:12px;color:var(--white);font-size:34px;font-weight:400;letter-spacing:.5px}
.brand-dot{width:30px;height:30px;border-radius:50%;background:var(--brand-green)}
.menu{position:absolute;right:78px;top:22px;display:flex;gap:50px;list-style:none;font-size:15px;color:var(--white)}
.menu .active{color:var(--accent)}

/* welcome */
.welcome{top:731px;height:312px;background:var(--panel);text-align:center}
.welcome h1{margin-top:48px;font-size:44px;font-weight:400;letter-spacing:2px}
.welcome p{width:900px;margin:20px auto 0;font-size:15px;line-height:26px;color:var(--ink-soft)}
.btn{display:inline-block;background:var(--btn-grey);color:var(--white);font-size:20px;border-radius:3px;text-align:center}
.welcome .btn{margin-top:30px;width:188px;height:52px;line-height:52px}

/* features */
.future{top:1043px;height:558px}
.future h2{text-align:center;margin-top:46px;font-size:40px;font-weight:400;letter-spacing:1px}
.feature{position:absolute;top:136px;width:323px}
.feature .photo{position:static;height:220px}
.feature h3{margin-top:14px;font-size:22px;font-weight:400}
.feature p{margin-top:6px;font-size:14px;line-height:24px;color:var(--ink-soft)}
.feature .btn{margin-top:14px;width:146px;height:44px;line-height:44px;font-size:17px}

/* audiences */
.audience{height:392px}
.audience h2{font-size:42px;font-weight:400;color:#444}
.audience .sub{font-size:20px;margin-top:2px}
.ticks{list-style:none;margin-top:26px;font-size:14px;color:var(--ink-soft)}
.ticks li{display:flex;align-items:center;gap:10px;height:29px}
.ticks svg{width:16px;height:16px;flex:none}
.audience .btn{margin-top:30px;width:194px;height:56px;line-height:56px}
.contractor{top:1601px;background:linear-gradient(90deg,var(--panel) 0%,#f4f4f4 60%,#e9e9e9 100%)}
.contractor .copy{position:absolute;left:78px;top:48px}
.company{top:1992px;background:linear-gradient(90deg,#3b3f44 0%,#8c9197 30%,#e9ebed 55%,#f3f4f5 100%)}
.company .copy{position:absolute;left:645px;top:40px}

/* blogs & team */
.stories{top:2384px;height:459px}
.col{position:absolute;top:50px;width:450px}
.col-head{display:flex;justify-content:space-between;align-items:center}
.col-head h2{font-size:32px;font-weight:400;color:#444}
.arrows{display:flex;gap:10px}
.arrows span{width:26px;height:26px;border-radius:50%;background:#cfcfcf;display:flex;align-items:center;justify-content:center}
.divider{position:absolute;left:604px;top:50px;width:1px;height:350px;background:var(--rule)}
.entry{position:absolute;left:0;display:flex;gap:20px}
.entry .thumb{width:105px;height:105px;flex:none;position:static}
.entry .avatar{width:84px;height:84px;border-radius:50%;flex:none;border:3px solid #e0e0e0}
.entry h3{font-size:19px;font-weight:400}
.entry h4{font-size:19px;font-weight:400}
.entry .role{font-size:15px;margin-top:2px}
.entry p{font-size:14px;line-height:24px;color:var(--ink-soft);margin-top:6px}
.entry time{display:block;font-size:13px;font-style:italic;color:var(--muted);margin-top:4px}

/* contact */
.contact{top:2843px;height:462px;background:linear-gradient(180deg,#2e3b47 0%,var(--night) 55%,#2d3a44 100%)}
.contact h2{text-align:center;margin-top:46px;font-size:38px;font-weight:400;color:var(--white)}
.field{position:absolute;background:var(--white);font-size:14px;color:var(--ink-soft);padding:11px 14px}
.submit{position:absolute;left:527px;top:358px;width:146px;height:44px;line-height:44px;background:var(--cta);color:var(--white);text-align:center;font-size:17px;border-radius:3px;letter-spacing:1px}

/* info + bar */
.info{top:3305px;height:148px;background:var(--panel)}
.info-item{position:absolute;top:37px;display:flex;align-items:center;gap:20px;font-size:15px;line-height:24px;color:var(--ink-soft)}
.ring{width:76px;height:76px;border-radius:50%;border:2px solid var(--brand-green);display:flex;align-items:center;justify-content:center;background:var(--white)}
.bar{top:3453px;height:63px;background:var(--bar);color:var(--white);font-size:15px;font-weight:700}
.bar .copyright{position:absolute;left:78px;top:20px}
.follow{position:absolute;right:78px;top:18px;display:flex;align-items:center;gap:22px}
.follow span.dot{width:22px;height:22px;border-radius:50%;background:#5a5a5a}
</style>
</head>
<body>

<header class="site-nav">
  <div class="brand"><span class="brand-dot"></span>quarrynest</div>
  <ul class="menu">
    <li class="active">HOME</li><li>HOW IT WORKS</li><li>ABOUT US</li><li>OUR PARTNERS</li><li>FAQS</li><li>BLOG</li>
  </ul>
</header>

<section class="hero" role="img" aria-label="Team of professionals gathered around a computer in a bright office, reviewing work together"></section>

<section class="welcome">
  <h1>WELCOME</h1>
  <p>Quarrynest is a unique marketplace providing contractors and companies a plaform to connect in real-time by exposing the "availability status". Through intuitive search Quarrynest will instantly shortlist available contractors with matching skill criteria. This is an invaluable tool for companies finding the right people at the right time and at low cost!!</p>
  <span class="btn">Read More</span>
</section>

<section class="future">
  <h2>THE FUTURE OF WORK IS HERE !</h2>
  <article class="feature" style="left:78px">
    <div class="photo" role="img" aria-label="Hands typing on a laptop keyboard" style="background:linear-gradient(135deg,#d9c7bc,#b9a69a 55%,#8d8480)"></div>
    <h3>Skill Match</h3>
    <p>Quarrynest has a secret sauce to find the right people to match the job requirements.</p>
    <span class="btn">Read More</span>
  </article>
  <article class="feature" style="left:438px">
    <div class="photo" role="img" aria-label="Hand holding a smartphone showing a calendar" style="background:linear-gradient(135deg,#c9a35a,#e4e2dc 50%,#6f8f3c)"></div>
    <h3>Calender</h3>
    <p>Uniquely Quarrynest has the visibility of contractors availability to work on projects.</p>
    <span class="btn">Read More</span>
  </article>
  <article class="feature" style="left:800px">
    <div class="photo" role="img" aria-label="Glass office towers against a blue sky" style="background:linear-gradient(135deg,#9cc4e8,#3f78b0 55%,#1c3d66)"></div>
    <h3>Location</h3>
    <p>Coupled with the skills &amp; availability the locations map you to the resources closest.</p>
    <span class="btn">Read More</span>
  </article>
</section>

<section class="audience contractor">
  <div class="copy">
    <h2>I’m a Contractor</h2>
    <div class="sub">If you are looking for work</div>
    <ul class="ticks">
      <li><svg viewBox="0 0 16 16"><path d="M2 8l4 4 8-9" fill="none" stroke="#666" stroke-width="2.4"/></svg>Increase utilisation by reducing idle time.</li>
      <li><svg viewBox="0 0 16 16"><path d="M2 8l4 4 8-9" fill="none" stroke="#666" stroke-width="2.4"/></svg>Choice of work based on offers received.</li>
      <li><svg viewBox="0 0 16 16"><path d="M2 8l4 4 8-9" fill="none" stroke="#666" stroke-width="2.4"/></svg>Increase earning potential by dealing direct with companies.</li>
    </ul>
    <span class="btn">Join for free</span>
  </div>
  <div class="photo" role="img" aria-label="Young woman sitting cross-legged working on a laptop" style="left:700px;top:10px;width:340px;height:382px;background:radial-gradient(ellipse at 50% 55%,#6f86ad 0%,#c7ccd6 45%,rgba(239,239,239,0) 72%)"></div>
</section>

<section class="audience company">
  <div class="photo" role="img" aria-label="Businessman on a phone call beside bright window blinds" style="left:0;top:0;width:600px;height:392px;background:linear-gradient(90deg,#3d4146,#7d8288 60%,rgba(230,232,234,0))"></div>
  <div class="copy">
    <h2>I’m a Company</h2>
    <div class="sub">If you are looking for people</div>
    <ul class="ticks">
      <li><svg viewBox="0 0 16 16"><path d="M2 8l4 4 8-9" fill="none" stroke="#666" stroke-width="2.4"/></svg>Save time by reviewing qualified shortlist of skills &amp; availability.</li>
      <li><svg viewBox="0 0 16 16"><path d="M2 8l4 4 8-9" fill="none" stroke="#666" stroke-width="2.4"/></svg>Predictable market talent pools and access to active resources.</li>
      <li><svg viewBox="0 0 16 16"><path d="M2 8l4 4 8-9" fill="none" stroke="#666" stroke-width="2.4"/></svg>Negotiate rates directly with the contractor.</li>
    </ul>
    <span class="btn">Join for free</span>
  </div>
</section>

<section class="stories">
  <div class="col" style="left:78px">
    <div class="col-head"><h2>RECENT BLOGS</h2>
      <div class="arrows"><span><svg width="10" height="10" viewBox="0 0 10 10"><path d="M7 1L3 5l4 4" fill="none" stroke="#fff" stroke-width="2"/></svg></span><span><svg width="10" height="10" viewBox="0 0 10 10"><path d="M3 1l4 4-4 4" fill="none" stroke="#fff" stroke-width="2"/></svg></span></div>
    </div>
    <article class="entry" style="top:70px">
      <div class="photo thumb" role="img" aria-label="Desk with papers and cloud sketches" style="background:linear-gradient(135deg,#f2f2f2,#9fb8d4 60%,#e0a84a)"></div>
      <div><h3>Top five cloud skills</h3><p>Job hunting this year? Here are the tech skills hiring managers want to see on your résumé. ..</p><time>3 march 2015</time></div>
    </article>
    <article class="entry" style="top:235px">
      <div class="photo thumb" role="img" aria-label="Tablet floating over a blue background" style="background:linear-gradient(135deg,#5fc3e6,#1d8fc4 60%,#0e5d8c)"></div>
      <div><h3>20 hot IT skills</h3><p>Job hunting this year? Here are the tech skills hiring managers want to see on your résumé. ..</p><time>3 march 2015</time></div>
    </article>
  </div>
  <div class="divider"></div>
  <div class="col" style="left:645px">
    <div class="col-head"><h2>MEET OUR TEAM</h2>
      <div class="arrows"><span><svg width="10" height="10" viewBox="0 0 10 10"><path d="M7 1L3 5l4 4" fill="none" stroke="#fff" stroke-width="2"/></svg></span><span><svg width="10" height="10" viewBox="0 0 10 10"><path d="M3 1l4 4-4 4" fill="none" stroke="#fff" stroke-width="2"/></svg></span></div>
    </div>
    <article class="entry" style="top:60px">
      <div class="avatar" role="img" aria-label="Portrait of the CEO" style="background:#9a7a66"></div>
      <div><h4>Marisol Ventrano</h4><div class="role">CEO &amp; CO-Founder</div><p>Marisol Ventrano is the co-founder of Quarrynest, established in 2014. Marisol has spent 20 years.</p></div>
    </article>
    <article class="entry" style="top:225px">
      <div class="avatar" role="img" aria-label="Portrait of the CTO" style="background:#8a8f96"></div>
      <div><h4>Dario Castellan</h4><div class="role">CTO &amp; CO-Founder</div><p>Building great businesses like The Keystone Circle which assist companies in solving complex business .</p></div>
    </article>
  </div>
</section>

<section class="contact" role="group" aria-label="Enquiry form over a dusk city scene with business people">
  <h2>Fill Our Contact Form for Enquiry</h2>
  <div class="field" style="left:211px;top:124px;width:229px;height:42px">Name</div>
  <div class="field" style="left:475px;top:124px;width:240px;height:42px">Phone</div>
  <div class="field" style="left:748px;top:124px;width:240px;height:42px">Email</div>
  <div class="field" style="left:211px;top:188px;width:777px;height:141px">Message</div>
  <div class="submit">SUBMIT</div>
</section>

<section class="info">
  <div class="info-item" style="left:258px">
    <div class="ring"><svg width="38" height="36" viewBox="0 0 38 36"><path d="M19 3L2 18h5v15h9v-10h6v10h9V18h5z" fill="#1d8a3f"/></svg></div>
    <div>Lorem ipsum dolor sit amet, consectetuer<br>adipiscing elit.</div>
  </div>
  <div class="info-item" style="left:742px">
    <div class="ring"><svg width="34" height="34" viewBox="0 0 24 24"><path d="M6.6 10.8a15.1 15.1 0 006.6 6.6l2.2-2.2c.3-.3.7-.4 1-.2 1.1.4 2.3.6 3.6.6.6 0 1 .4 1 1V20c0 .6-.4 1-1 1A17 17 0 013 4c0-.6.4-1 1-1h3.5c.6 0 1 .4 1 1 0 1.3.2 2.5.6 3.6.1.3 0 .7-.2 1z" fill="#1d8a3f"/></svg></div>
    <div>123-555-018</div>
  </div>
</section>

<footer class="bar">
  <div class="copyright">© THE QUARRYNEST -2016.All Rights Reserved.</div>
  <div class="follow">Follow us at <span class="dot"></span><span class="dot"></span><span class="dot"></span></div>
</footer>

</body>
</html>
```